Double-sided half page marketing handout for professional association conference

We need a collatoral piece that will go into conference attendees' registration packets. Handout will be double-sided, half-letter-sized page. Working print area is 8.1" by 5.3" for each side. Can be laid out either vertically or horizontally.

One side of the piece will be focused on my firm's contact information and broad scope of services:

Contact Information:
Velmont Partners LLC
Local Government Consultants
415-630-2918
www.velmontpartners.example
info@velmontpartners.example

Services:
Bond Rating Assessments
Economic Development Consulting
Executive Dashboards
Public Policy Analysis
Governance Training & Support
Strategic Planning & Performance Management

The other side of the piece will focus on the Bond Rating Assessments (see http://www.velmontpartners.example/Pages/Bond-Rating-Assessments.aspx and attachments for more detail). This side should contain the text:

"Considering issuing debt? Bond ratings make a difference. Did you know that on an average $20 million GO debt issuance a one rating-level difference can easily equate to over $350,000 in interest cost-savings under normal market conditions?

The ratings agencies use a combined quantitative and qualitative approach to arrive at your bond rating. Our Bond Ratings Assessment shows you precisely what the agencies are looking at, provides advice as to how to frame the conversation during ratings calls, and identifies both strategic opportunities to provide upgrade pressure and specific threats that may lead to a downgrade. Call or email us to find out more or to get an example assessment."

Go to www.velmontpartners.example and see attached files for logo and a recent winning ArtHive 1/4 page advertisement for style guidance.

Target Market(s)

Highly-educated, conservative local government executives.

Industry/Entity Type

Marketing

Font styles to use
Sans Serif

Colors
3277b5
85acd3
ffffff

Requirements
Must have
• Our logo, our contact information, basic information stated in Project Description. Feel free to modify language to make more clear or understandable.
Nice to have
• We rather not just a text piece - bringing in some graphical elements would be very nice.

```html
<!DOCTYPE html>
<html lang="en">
<head>
<meta charset="utf-8">
<title>Velmont Partners LLC – Contact &amp; Services Handout</title>
<link href="https://fonts.googleapis.com/css2?family=Lato:wght@300;700;900&family=Roboto+Condensed:wght@700&display=swap" rel="stylesheet">
<style>
  :root {
    --brand-blue: #3277b5;
    --brand-blue-light: #85acd3;
    --band-top: #7aa5d6;
    --white: #ffffff;
    --ink: #3a3a3a;
    --silhouette: #e4e4e4;
    --stage: #ebe8e1;
  }
  * { margin: 0; padding: 0; box-sizing: border-box; }
  html, body {
    width: 1200px; height: 953px; overflow: hidden;
    background: var(--stage);
  }
  .handout {
    position: absolute; left: 335px; top: 70px;
    width: 530px; height: 810px;
    background: var(--white);
    font-family: "Lato", sans-serif;
  }
  .brand {
    position: absolute; left: 0; right: 0; top: 22px;
    text-align: center;
    font-family: "Lato", sans-serif;
    font-weight: 700; font-size: 46px; line-height: 50px;
    color: var(--ink);
  }
  .contact-band {
    position: absolute; left: 0; right: 0; top: 145px; height: 220px;
    background: linear-gradient(to bottom, var(--band-top) 0%, var(--brand-blue) 22%, var(--brand-blue) 100%);
    color: var(--white); text-align: center;
  }
  .contact-band .heading {
    position: absolute; left: 0; right: 0; top: 15px;
    font-weight: 700; font-size: 24px;
  }
  .contact-band .line {
    position: absolute; left: 0; right: 0;
    font-weight: 300; font-size: 23px;
  }
  .contact-band .firm { top: 46px; }
  .contact-band .tagline { top: 76px; }
  .contact-band .phone {
    position: absolute; left: 0; right: 0; top: 107px;
    font-weight: 700; font-size: 28px;
    display: flex; justify-content: center; align-items: center; gap: 10px;
  }
  .contact-band .web {
    position: absolute; left: 0; right: 0;
    font-weight: 700; font-size: 22px;
  }
  .contact-band .url { top: 144px; }
  .contact-band .email { top: 174px; }
  .thinker-figure {
    position: absolute; left: 75px; top: 395px; width: 365px; height: 398px;
    background: linear-gradient(to bottom, #e9e9e9, var(--silhouette));
    border-radius: 180px 180px 0 0;
  }
  .services {
    position: absolute; left: 0; right: 0; top: 512px;
    text-align: center; color: var(--brand-blue);
  }
  .services h2 {
    font-family: "Lato", sans-serif; font-weight: 900; font-size: 26px;
    margin-bottom: 4px;
  }
  .services ul { list-style: none; }
  .services li {
    font-family: "Roboto Condensed", sans-serif; font-weight: 700;
    font-size: 19px; line-height: 29px; letter-spacing: -0.3px;
  }
  .services li.two-line { line-height: 20px; margin-top: 4px; }
  .footer-rule {
    position: absolute; left: 0; right: 0; bottom: 0; height: 17px;
    background: var(--brand-blue-light);
  }
</style>
</head>
<body>
  <main class="handout">
    <div class="brand">Velmont Partners<br>LLC</div>

    <section class="contact-band">
      <div class="heading">Contact Information:</div>
      <div class="line firm">Velmont Partners LLC</div>
      <div class="line tagline">Local Government Consultants</div>
      <div class="phone">
        <svg width="16" height="28" viewBox="0 0 16 28" aria-hidden="true">
          <rect x="1" y="3" width="14" height="24" rx="2" fill="none" stroke="#fff" stroke-width="1.6"/>
          <line x1="11" y1="3" x2="11" y2="0" stroke="#fff" stroke-width="1.6"/>
          <rect x="3.5" y="6" width="9" height="7" fill="#fff"/>
          <g fill="#fff">
            <rect x="3.5" y="15" width="2.4" height="2"/><rect x="6.8" y="15" width="2.4" height="2"/><rect x="10.1" y="15" width="2.4" height="2"/>
            <rect x="3.5" y="18.5" width="2.4" height="2"/><rect x="6.8" y="18.5" width="2.4" height="2"/><rect x="10.1" y="18.5" width="2.4" height="2"/>
            <rect x="3.5" y="22" width="2.4" height="2"/><rect x="6.8" y="22" width="2.4" height="2"/><rect x="10.1" y="22" width="2.4" height="2"/>
          </g>
        </svg>
        <span>415-630-2918</span>
      </div>
      <div class="web url">www.velmontpartners.example</div>
      <div class="web email">info@velmontpartners.example</div>
    </section>

    <div class="thinker-figure" role="img" aria-label="Grey profile silhouette of a human head with gears and a dollar sign turning inside"></div>

    <section class="services">
      <h2>Services:</h2>
      <ul>
        <li>Bond Rating Assessments</li>
        <li>Economic Development Consulting</li>
        <li>Executive Dashboards</li>
        <li>Public Policy Analysis</li>
        <li>Governance Training &amp; Support</li>
        <li class="two-line">Strategic Planning &amp;<br>Performance Management</li>
      </ul>
    </section>

    <div class="footer-rule"></div>
  </main>
</body>
</html>
```